" A RUMO CERTO é uma consultoria de processos e tecnologia da informação com mais de 18 anos de mercado. Somos especialistas em análise, modelagem e otimização de processos para gestão de SST (Segurança e Saúde do Trabalho). Realizamos projetos e implementação de soluções para a área de SST, Recursos Humanos, construção de indicadores (KPIs) e entregamos soluções eficientes para o negócio de nossos clientes. "

```html
<!DOCTYPE html>
<html lang="pt-BR">
<head>
<meta charset="utf-8">
<title>Assinatura de e-mail – Rumo Certo</title>
<link href="https://fonts.googleapis.com/css2?family=Open+Sans:wght@300;400;600&display=swap" rel="stylesheet">
<style>
  :root {
    --paper: #ffffff;
    --frame: #dcdcdc;
    --ink: #6b6b6b;
    --ink-dark: #4a4a4a;
    --accent: #f0a030;
    --divider: #b8b8b8;
    --icon: #8a8a8a;
  }
  html, body {
    margin: 0;
    padding: 0;
    width: 1200px;
    height: 1200px;
    overflow: hidden;
    background: var(--paper);
    font-family: "Open Sans", Arial, sans-serif;
  }
  .canvas {
    position: relative;
    width: 1200px;
    height: 1200px;
  }
  .signature {
    position: absolute;
    left: 79px;
    top: 482px;
    width: 1042px;
    height: 236px;
    border: 2px solid var(--frame);
    box-sizing: border-box;
    background: var(--paper);
  }
  .portrait {
    position: absolute;
    left: 12px;
    top: 16px;
    width: 202px;
    height: 202px;
    border-radius: 50%;
    background: radial-gradient(circle at 50% 40%, #c9d4dc 0%, #8e9aa6 55%, #3b4450 100%);
  }
  .divider {
    position: absolute;
    left: 255px;
    top: 34px;
    width: 3px;
    height: 180px;
    background: var(--divider);
  }
  .arrow {
    position: absolute;
    left: 272px;
    top: 30px;
    width: 40px;
    height: 40px;
  }
  .name {
    position: absolute;
    left: 318px;
    top: 16px;
    margin: 0;
    font-size: 48px;
    font-weight: 300;
    color: var(--ink);
    line-height: 1;
    white-space: nowrap;
  }
  .name strong { font-weight: 600; }
  .role {
    position: absolute;
    left: 320px;
    top: 68px;
    margin: 0;
    font-size: 23px;
    font-weight: 400;
    color: var(--ink);
  }
  .contact {
    position: absolute;
    left: 320px;
    top: 120px;
    margin: 0;
    padding: 0;
    list-style: none;
    font-size: 17.5px;
    line-height: 26.5px;
    color: var(--ink);
  }
  .contact .label { color: var(--ink-dark); margin-right: 8px; }
  .brand {
    position: absolute;
    left: 688px;
    top: 84px;
    display: flex;
    align-items: center;
    gap: 12px;
  }
  .brand-dot {
    width: 22px;
    height: 22px;
    border-radius: 50%;
    background: var(--accent);
  }
  .brand-name {
    font-size: 46px;
    font-weight: 400;
    color: var(--ink);
    letter-spacing: 1px;
    white-space: nowrap;
    line-height: 1;
  }
  .social {
    position: absolute;
    left: 770px;
    top: 178px;
    display: flex;
    gap: 11px;
  }
  .social span {
    width: 30px;
    height: 30px;
    border-radius: 50%;
    background: var(--icon);
  }
</style>
</head>
<body>
<div class="canvas">
  <section class="signature">
    <div class="portrait" role="img" aria-label="Foto de retrato da assistente administrativa"></div>
    <div class="divider"></div>
    <svg class="arrow" viewBox="0 0 40 40" aria-hidden="true">
      <path d="M6 6 L30 30 M30 12 L30 30 L12 30" fill="none" stroke="var(--accent)" stroke-width="6" stroke-linecap="square"/>
    </svg>
    <h1 class="name">Clara <strong>Mendes</strong></h1>
    <p class="role">Assistente Administrativo</p>
    <ul class="contact">
      <li><span class="label">Phone</span>(11) 3456-7890</li>
      <li><span class="label">Address</span>Av das Acácias, 2740</li>
      <li>Conj 318 - São Paulo - 01310-000</li>
      <li><span class="label">WebSite</span>www.rumocerto.com.br</li>
    </ul>
    <div class="brand">
      <span class="brand-dot"></span>
      <span class="brand-name">RUMO CERTO</span>
    </div>
    <div class="social" aria-label="Redes sociais">
      <span></span><span></span><span></span><span></span><span></span>
    </div>
  </section>
</div>
</body>
</html>
```